Meadowlane Women's Health - patient info e-book

We require an easy-edit template for a patient e-book that can easily be converted into a pdf for distribution through our website.
**We will be using Adobe InDesign, so compatible designs ONLY will be considered**
Target Market(s)
Women aged 28-55
Industry/Entity Type
Health
Font styles to use
Sans Serif
Colors
886aae
b8a6cd
d3a5cc
b768aa
ffffff
ecdaeb
b868aa
fbd4d5
f59296
Requirements
Must have
- Editable fields for text
- Easy to convert to PDF
- Easy to insert/change stock photos
- Should incorporate the attached logo

```html
<!DOCTYPE html>
<html lang="en">
<head>
<meta charset="utf-8">
<title>Meadowlane Women's Health – E-News</title>
<link href="https://fonts.googleapis.com/css2?family=Cabin:wght@400&family=Source+Sans+3:wght@600;700&family=Tinos:ital@0;1&display=swap" rel="stylesheet">
<style>
  :root {
    --purple: #886aae;
    --lavender: #b8a6cd;
    --orchid: #d3a5cc;
    --plum: #b768aa;
    --white: #ffffff;
    --blush: #ecdaeb;
    --pink: #fbd4d5;
    --coral: #f59296;
    --ink: #1a1a1a;
  }
  * { margin: 0; padding: 0; box-sizing: border-box; }
  html, body { width: 927px; height: 1200px; overflow: hidden; background: var(--white); }
  .page { position: relative; width: 927px; height: 1200px; overflow: hidden; background: var(--white); color: var(--ink); }

  .masthead-band {
    position: absolute; left: 0; top: 0; width: 927px; height: 108px;
    background: var(--purple);
    box-shadow: 0 4px 8px rgba(60, 40, 90, 0.25);
  }
  .band-label {
    position: absolute; top: 60px;
    font-family: "Source Sans 3", sans-serif; font-weight: 700; font-size: 24px;
    color: var(--white); letter-spacing: 0.2px;
  }
  .band-label.edition { left: 338px; }
  .band-label.date { right: 54px; }

  .brand-disc {
    position: absolute; left: 58px; top: 61px; width: 242px; height: 242px; border-radius: 50%;
    background:
      radial-gradient(circle at 70% 30%, rgba(150, 230, 190, 0.55) 0%, rgba(150, 230, 190, 0) 45%),
      radial-gradient(circle at 40% 75%, #e9a6cf 0%, rgba(233, 166, 207, 0) 60%),
      linear-gradient(160deg, #9ec9d8 0%, #c9b6dd 45%, #f0b3d4 100%);
  }

  .title {
    position: absolute; left: 360px; top: 150px; width: 492px;
    font-family: "Cabin", sans-serif; font-weight: 400; font-size: 38px; line-height: 52px;
    text-align: center; text-transform: uppercase; color: #111; letter-spacing: 0.5px;
  }

  .headline {
    position: absolute; left: 55px; top: 318px;
    font-family: "Source Sans 3", sans-serif; font-weight: 700; font-size: 57px; line-height: 64px;
    color: var(--purple); letter-spacing: -0.3px;
  }

  .column {
    position: absolute; top: 412px; width: 255px;
    font-family: "Tinos", serif; font-size: 15.6px; line-height: 20.6px;
    letter-spacing: -0.05px;
    text-align: justify; hyphens: manual;
  }
  .column.c1 { left: 56px; }
  .column.c2 { left: 335px; }
  .column.c3 { left: 618px; }
  .column p { text-indent: 22px; margin-bottom: 6px; }
  .column p.carry { text-indent: 0; }
  .column p.runs-on { text-align-last: justify; margin-bottom: 0; }

  .continued {
    position: absolute; right: 55px; top: 698px;
    font-family: "Tinos", serif; font-style: italic; font-size: 15.6px;
  }

  .feature-photo {
    position: absolute; left: 56px; top: 779px; width: 535px; height: 289px;
    border: 1.5px solid #111;
    background:
      linear-gradient(180deg, rgba(0,0,0,0) 0%, rgba(0,0,0,0) 70%, #5a4a50 80%, #3b3440 90%, #6b6a80 100%),
      linear-gradient(180deg, #5d6a86 0%, #8a8aa6 25%, #c9a7b8 45%, #f2c1a0 60%, #f7d7b4 70%);
  }
  .caption {
    position: absolute; left: 56px; top: 1082px; width: 535px;
    font-family: "Tinos", serif; font-style: italic; font-size: 15px; line-height: 21px; text-align: center;
  }

  .contents-panel {
    position: absolute; left: 620px; top: 757px; width: 251px; height: 381px;
    background: var(--pink);
    clip-path: polygon(
      8px 0, calc(100% - 8px) 0, calc(100% - 8px) 8px, 100% 8px,
      100% calc(100% - 8px), calc(100% - 8px) calc(100% - 8px), calc(100% - 8px) 100%,
      8px 100%, 8px calc(100% - 8px), 0 calc(100% - 8px), 0 8px, 8px 8px);
  }
  .contents-title {
    position: absolute; left: 0; top: 14px; width: 100%;
    font-family: "Source Sans 3", sans-serif; font-weight: 600; font-size: 28px; text-align: center; color: #111;
  }
  .contents-rule {
    position: absolute; left: 13px; top: 54px; width: 216px; height: 4px; background: var(--coral);
  }
  .contents-list {
    position: absolute; left: 13px; top: 70px; width: 216px; list-style: none;
    font-family: "Source Sans 3", sans-serif; font-weight: 700; font-size: 19px; line-height: 28px; color: #111;
  }
  .contents-list li { margin-bottom: 8px; }
  .entry-line { display: flex; align-items: baseline; white-space: nowrap; }
  .leader { flex: 1; overflow: hidden; margin: 0 3px; letter-spacing: 1px; }
  .leader::before { content: "....................................................."; }
</style>
</head>
<body>
<div class="page">
  <div class="masthead-band"></div>
  <div class="band-label edition">E-News</div>
  <div class="band-label date">May 2015</div>

  <div class="brand-disc" role="img" aria-label="Meadowlane Women's Health emblem area, soft aurora gradient"></div>

  <h1 class="title">Meadowlane Women’s<br>Health</h1>

  <h2 class="headline">Peris aut modis sam quae</h2>

  <div class="column c1">
    <p>Ore, sequia sam aut adi dicium ex est, officae cullabo rationsed que ven&shy;daes quiatum imentoribus eum lab il eium volum non numet reperchil inul&shy;lac caborum ut exceati vente rae vo&shy;luptatiis eum ipsa vendesciam dolup&shy;tutio. Em fuga. Ibuscid usdamus aut quatem nus.</p>
    <p class="runs-on">Edit harchit officil inverum etum sequi as pellique rem quibeat ecesti&shy;ae. Tas eiur, consectus dolorecabo. Um volupti orenem excepe cullaudi&shy;ate nihic te et a plabore que nonsed et aboribus maximus sandunt quod mod etur apis aut quasperem laborer spellest ea qui ommos pliciis ra vol-</p>
  </div>

  <div class="column c2">
    <p class="carry">lessus quatem volorpor repedipsa plic&shy;ipitate volorestium ut adionsedit, sunt apientem faccus audam el issintior aut quias dolupta prem everatiurit, occus et ped que volorpor maximi, officides aut Us eari dolupta si delluptas deles&shy;tia doluptia quam autas consequunt, tempore pudanist, quiam, etur rerum a quiam audit que nonet, od moditam quis aut autem dolorem. Nam quia nis quamet mincient acculparibus seque con conem quissit ut officiunti blaex&shy;plantur am doloreptat.</p>
    <p class="runs-on">Ces aute liqui ducit officitat om&shy;noluptur aut re, sandipsant.Omnit ati omniend untempe libus, omnia volum</p>
  </div>

  <div class="column c3">
    <p class="carry">eum cus est perror mod mo quistiasi dolupta voluptaquia vendandes ius sedit laborerum hitem simagnis id que nia qui doluptatur sequi aut vol&shy;uptatem iumet volut entorec tassimo lorectas dellor aut ra pa et, sequatat.</p>
    <p class="runs-on">Poreste moditat volo beritam en&shy;imagnation culparum ex ellorume vo&shy;luptatum sumquo erovitio eate sumet exerferferum nonetur molupta audis corecti dit que et eum dolestia cor re&shy;pelest est et perioribusa con porisciis sapis et plit, qui opti odi aliquammolut</p>
  </div>

  <div class="continued">continued on page 4</div>

  <div class="feature-photo" role="img" aria-label="City skyline across the water at sunset under a pink and violet cloudy sky"></div>
  <p class="caption">Nam que pla simille catibus, siminis eat.<br>consed qui nonsedist late nullaccab int ma exeriam, simpor seque perciusae im</p>

  <aside class="contents-panel">
    <div class="contents-title">Inside This Issue</div>
    <div class="contents-rule"></div>
    <ul class="contents-list">
      <li class="entry-line"><span>Departments</span><span class="leader"></span><span>4</span></li>
      <li><div>Upcoming Health</div><div class="entry-line"><span>Screenings</span><span class="leader"></span><span>2</span></div></li>
      <li class="entry-line"><span>For Your Health</span><span class="leader"></span><span>3</span></li>
    </ul>
  </aside>
</div>
</body>
</html>
```